Brenmoor Ridge Auto Auction 22nd Anniversary

We are a public auto auction based in Pennsylvania looking for an automotive themed post card design for our 22nd Anniversary. The design must include both a front and a back. It must be in a standard horizontal post card size (vertical post cards use different amounts of postage). Jpeg images of our 2 logos, the 21st anniversary, and the 20th anniversary are included (the office favorite is the 21st). Logo use is optional. Matching the theme with the logo is recommended but not required.

Target Market(s)

New and Used car dealers in Pennsylvania.

Industry/Entity Type

Automotive

Requirements
Nice to have
• The logo is recommended to have
Should not have
• Cartoonish figures.

```html
<!DOCTYPE html>
<html lang="en">
<head>
<meta charset="utf-8">
<title>Brenmoor Ridge Auto Auction – 22nd Anniversary Auction</title>
<link href="https://fonts.googleapis.com/css2?family=Arimo:wght@400;700&family=Archivo+Black&family=Allura&family=Playfair+Display:wght@700&display=swap" rel="stylesheet">
<style>
  :root {
    --sky-top: #f4b8a8;
    --sky-mid: #f8cf9a;
    --sun-glow: #fbe6a6;
    --field: #a4ad4a;
    --field-dark: #6f6c2e;
    --road: #8f8478;
    --road-dark: #3a2e29;
    --car-red: #c3312a;
    --car-red-dark: #8e211c;
    --ink: #111111;
    --white: #ffffff;
    --orange: #f26a1b;
    --script-blue: #86c9f2;
    --script-edge: #16385a;
    --fin-blue: #3aa6f0;
    --gold: #d2a95e;
    --gold-light: #f6e0a8;
    --gold-dark: #8a6424;
    --panel: #5ff0fa;
  }
  * { margin: 0; padding: 0; box-sizing: border-box; }
  html, body { width: 1200px; height: 930px; overflow: hidden; background: #fff; }
  .postcard {
    position: relative;
    width: 1200px;
    height: 930px;
    overflow: hidden;
    font-family: "Arimo", Arial, sans-serif;
  }
  .scene-photo {
    position: absolute; inset: 0;
    background:
      radial-gradient(ellipse 560px 250px at 830px 720px, var(--car-red) 0%, var(--car-red-dark) 62%, rgba(142,33,28,0) 80%),
      linear-gradient(180deg,
        var(--sky-top) 0%,
        #f7c6a2 18%,
        var(--sky-mid) 30%,
        var(--sun-glow) 37%,
        var(--field) 43%,
        var(--field-dark) 56%,
        var(--road) 66%,
        #6a5a4e 82%,
        var(--road-dark) 100%);
  }

  /* brand block in the top-left circle area */
  .brand {
    position: absolute; left: 42px; top: 70px; width: 300px;
    display: flex; flex-direction: column; align-items: center; gap: 16px;
    text-align: center;
  }
  .brand-dot {
    width: 90px; height: 90px; border-radius: 50%;
    background: var(--ink);
  }
  .brand-name {
    font-weight: 700; font-size: 34px; line-height: 1.15;
    color: var(--ink);
  }

  .headline {
    position: absolute; left: 500px; top: 78px; width: 640px;
    text-align: center; color: var(--ink);
  }
  .headline-top { white-space: nowrap; line-height: 1; }
  .headline-year { font-size: 90px; line-height: 1; vertical-align: bottom; }
  .headline-year sup { font-size: 50px; vertical-align: 38px; }
  .headline-script {
    font-family: "Allura", cursive;
    font-size: 104px; line-height: 1; vertical-align: bottom;
    color: var(--script-blue);
    -webkit-text-stroke: 2.5px var(--script-edge);
    paint-order: stroke fill;
  }
  .headline-main {
    font-family: "Archivo Black", sans-serif;
    font-size: 96px; line-height: 1;
    margin-top: 8px;
  }

  .pitch {
    position: absolute; left: 572px; top: 322px; width: 596px;
    text-align: center; color: var(--white);
  }
  .pitch-lead {
    font-size: 48px; line-height: 1.1;
    -webkit-text-stroke: 1.5px var(--ink); paint-order: stroke fill;
  }
  .pitch-accent {
    font-weight: 700; font-size: 76px; line-height: 1.05; letter-spacing: -1px;
    color: var(--orange);
    -webkit-text-stroke: 3px var(--white); paint-order: stroke fill;
  }
  .pitch-accent .amp { color: var(--white); }
  .pitch-sub {
    font-weight: 700; font-size: 40px; letter-spacing: 14px; line-height: 1.1;
    -webkit-text-stroke: 2px var(--ink); paint-order: stroke fill;
  }

  .big-number {
    position: absolute; left: 30px; top: 182px;
    font-family: "Playfair Display", serif; font-weight: 700;
    font-size: 392px; line-height: 1; letter-spacing: -8px;
    color: var(--gold);
    -webkit-text-stroke: 3px var(--gold-dark);
    text-shadow: 4px 4px 0 var(--gold-light), 0 0 22px rgba(150,120,255,.7);
  }

  .schedule {
    position: absolute; left: 35px; top: 600px;
    width: 457px; height: 218px;
    background: var(--panel); border: 2px solid #222; border-radius: 30px;
    display: flex; flex-direction: column; justify-content: center;
    text-align: center; font-size: 32px; line-height: 1.36; color: var(--ink);
  }

  .financing {
    position: absolute; left: 610px; top: 588px; width: 520px;
    text-align: center;
    font-family: "Archivo Black", sans-serif; font-size: 37px; line-height: 1.22;
    color: var(--fin-blue);
    -webkit-text-stroke: 4px var(--ink); paint-order: stroke fill;
  }

  .website {
    position: absolute; left: 0; right: 0; top: 850px;
    text-align: center; color: var(--white);
    font-size: 44px; letter-spacing: 8.5px;
    -webkit-text-stroke: 2px var(--ink); paint-order: stroke fill;
  }
</style>
</head>
<body>
  <main class="postcard">
    <div class="scene-photo" role="img" aria-label="Sunset over a country road and farm fields with a red vintage convertible muscle car with white racing stripes"></div>

    <div class="brand">
      <span class="brand-dot"></span>
      <span class="brand-name">Brenmoor Ridge Auto Auction</span>
    </div>

    <header class="headline">
      <div class="headline-top"><span class="headline-year">22<sup>TH</sup></span><span class="headline-script">Anniversary</span></div>
      <div class="headline-main">AUCTION</div>
    </header>

    <div class="big-number">22</div>

    <section class="pitch">
      <p class="pitch-lead">We Do Business with</p>
      <p class="pitch-accent">BIGGEST<span class="amp">&amp;</span>BEST</p>
      <p class="pitch-sub">NEW CAR STORES</p>
    </section>

    <div class="schedule">
      <p>Auction Start at<br>5:30 pm</p>
      <p>Gates Open at<br>4:00 pm</p>
    </div>

    <p class="financing">AUTOLANE, KFS, RFC,<br>&amp; TMC FINANCING</p>

    <p class="website">www.brenmoorridgeautoauction.com</p>
  </main>
</body>
</html>
```